I need a cd cover for a new pop rock album called "Letters from the tin harbour"
The main color of the artwork shall obviously be orange. The artwork shouldn't be too "obvious", but it would be better something a bit abstract.
Please remember that it is a Music Cd Cover, so do not send business logo or advertisement images.

It's a pop rock album, so the target customers are young and adult people from 15-60 years old

• Orange as main colour
The Artist name is: Tomas Verhelst
The Title: Letters from the tin harbour
• Not too cheesy or dreamy images please. No simple sunset or sunrise pics

```html
<!DOCTYPE html>
<html lang="en">
<head>
<meta charset="utf-8">
<title>Letters from the tin harbour — Tomas Verhelst</title>
<link rel="stylesheet" href="https://fonts.googleapis.com/css2?family=Special+Elite&display=swap">
<style>
  :root {
    --sky-blue: #2f6fc4;
    --peel-orange: #f7a21e;
    --peel-amber: #fcbc2a;
    --peel-deep: #f07a12;
    --band-red: #f0121f;
    --band-indigo: #3b2a9c;
    --type-amber: #f8b02c;
  }
  * { box-sizing: border-box; margin: 0; padding: 0; }
  html, body {
    width: 1200px;
    height: 1089px;
    overflow: hidden;
    background: var(--peel-orange);
  }
  .cover {
    position: relative;
    width: 1200px;
    height: 1089px;
    overflow: hidden;
  }
  .cloud-artwork {
    position: absolute;
    inset: 0;
    background:
      radial-gradient(ellipse 260px 150px at 62% 10%, rgba(47,111,196,0.85), rgba(47,111,196,0) 100%),
      radial-gradient(ellipse 220px 140px at 10% 45%, rgba(47,111,196,0.8), rgba(47,111,196,0) 100%),
      radial-gradient(ellipse 240px 130px at 88% 55%, rgba(47,111,196,0.75), rgba(47,111,196,0) 100%),
      radial-gradient(ellipse 260px 120px at 40% 88%, rgba(47,111,196,0.75), rgba(47,111,196,0) 100%),
      radial-gradient(ellipse 420px 320px at 50% 50%, var(--peel-amber), rgba(252,188,42,0) 100%),
      radial-gradient(ellipse 380px 300px at 15% 90%, var(--peel-deep), rgba(240,122,18,0) 100%),
      radial-gradient(ellipse 380px 300px at 90% 90%, var(--peel-deep), rgba(240,122,18,0) 100%),
      var(--peel-orange);
  }
  .title-block {
    position: absolute;
    left: 170px;
    top: 430px;
    width: 860px;
    height: 230px;
    transform: rotate(-36deg);
    transform-origin: center;
  }
  .band { position: absolute; }
  .band--indigo {
    left: 0;
    top: 100px;
    width: 860px;
    height: 130px;
    background: var(--band-indigo);
  }
  .band--red {
    left: 150px;
    top: 8px;
    width: 580px;
    height: 150px;
    background: var(--band-red);
  }
  .band-knot {
    position: absolute;
    left: 660px;
    top: -40px;
    width: 104px;
    height: 104px;
    border-radius: 50%;
    background: var(--band-red);
  }
  .line {
    position: absolute;
    font-family: "Special Elite", "Courier New", monospace;
    font-weight: 400;
    font-size: 48px;
    line-height: 1;
    letter-spacing: 1px;
    color: var(--type-amber);
    white-space: nowrap;
  }
  .line--title-1 { left: 175px; top: 30px; }
  .line--the     { left: 28px;  top: 100px; }
  .line--title-2 { left: 175px; top: 100px; }
  .line--artist  { left: 175px; top: 170px; }
</style>
</head>
<body>
  <main class="cover">
    <div class="cloud-artwork" role="img" aria-label="Photographic artwork of orange citrus-peel shapes floating like clouds on a blue sky"></div>

    <div class="title-block">
      <div class="band band--indigo"></div>
      <div class="band band--red"></div>
      <div class="band-knot"></div>
      <h1 class="line line--title-1">Letters from</h1>
      <span class="line line--the">the</span>
      <span class="line line--title-2">tin harbour</span>
      <h2 class="line line--artist">Tomas Verhelst</h2>
    </div>
  </main>
</body>
</html>
```